Pharmacy and Travel Clinic Leaflet

We are an established pharmacy and gift shop which also runs a travel and vaccination clinic. We have had the same leaflet for a couple of years and would like to refresh it for the following reasons:
We have rebranded our travel and vaccination clinic as Brackenmoor Travel Clinic with its own dedicated website (www.brackenmoortravelclinic.co.uk).
We have made changes to our prices that need to be reflected in the new leaflet.

The original leaflet was a little information heavy as the service was new and we would like the new leaflet to be more visually appealing with the pharmacy side highlighting our services and using the colours of our logo (purple and green) and the vaccination side using the colours of our travel clinic logo (navy blue, light blue, red and white). Logo's are attached in a variety of formats as I have no idea what is most useful.

I will upload some images that may assist with the design, as well as updated text for the pharmacy leaflet and the new prices and text required for the vaccination side. I do not expect all of the images to be used.

The leaflet is to be two-sided, which we will print in A3 and possibly enlarge to use on a large A-Board.

I would like to receive the files in format(s) that can be sent to a printers and also added to our website to display our prices.

I have attached a copy of our existing leaflet for reference.

If any information requires clarification or there are files that you need to improve the design then please let me know and I will try to sort that out.

P.S. The font we usually use now is Orkney

I have an extra requirement if this is possible. On the pharmacy services side of the leaflet I would like the tagline Providing QHA services at the bottom right of the leaflet. It can go on the bottom left if necessary. It doesn't need to be large. It needs to be in the black font (Arial or Helvetica) with the QHA logo in blue. I have attached a link to the QHA logo website and files are now uploaded to give you an idea of what we need.
The Providing QHA services and logo need to be exactly as shown in the uploads. The QHA do not allow their logo to be used creatively.
https://www.central.qha-care.org/qhaidentity/identity-guidelines/service-branding/

Thanks for all the submissions. They were very good but I had to choose one.

Target Market(s)

All ages from young students through to pensioners.

Industry/Entity Type

Pharmacy

Font styles to use
Sans Serif

Colors
9bcb3c
6c459b
ec1f27
0255a3
ffffff

Requirements
Must have
• Leaflet needs to be professional yet still be bold enough to stand out.
• Premium look using colours stated in brief. Colours differ for pharmacy side and travel clinic side. Please don't mix pharmacy and travel colours
Nice to have
• Please use the logos and tie the scheme in with those colours. Where the prices of vaccines are listed they need to be clear
• The Providing QHA services line and logo need to be exactly as shown in the uploads. The QHA do not allow their logo to be used creatively.
Should not have
• Must not be too informal. No comedy fonts

```html
<!DOCTYPE html>
<html lang="en">
<head>
<meta charset="utf-8">
<title>Brackenmoor Travel Clinic – Travel Vaccines</title>
<link href="https://fonts.googleapis.com/css2?family=Montserrat:wght@700;800&family=Didact+Gothic&display=swap" rel="stylesheet">
<style>
  :root{
    --navy:#0255a3;
    --sky:#5bc0eb;
    --red:#ec1f27;
    --purple:#6c459b;
    --ink:#2b2b2b;
    --paper:#eeeff1;
    --rule:#7a5aa8;
    --footer-dark:#3a3a3c;
    --white:#ffffff;
  }
  *{margin:0;padding:0;box-sizing:border-box}
  html,body{width:848px;height:1200px;overflow:hidden;background:var(--paper)}
  body{font-family:"Didact Gothic",Arial,sans-serif;color:var(--ink)}
  .leaflet{position:relative;width:848px;height:1200px;overflow:hidden;
    background:linear-gradient(180deg,#f4f4f6 0%,var(--paper) 100%)}
  .header{position:absolute;left:0;top:0;width:848px;height:320px}
  .brand{position:absolute;left:463px;top:112px;transform:translateX(-50%);
    display:flex;align-items:center;gap:10px;white-space:nowrap}
  .brand-dot{width:22px;height:22px;border-radius:50%;background:var(--sky)}
  .brand-name{font-family:"Didact Gothic",Arial,sans-serif;font-size:22px;color:var(--white);letter-spacing:1px}
  .title{position:absolute;left:0;width:848px;top:300px;text-align:center;
    font-family:"Montserrat",Arial,sans-serif;font-weight:800;font-size:50px;letter-spacing:-1px;color:#333}
  .title span{color:var(--navy)}
  .price-list{position:absolute;left:39px;width:422px;list-style:none}
  .price-list li{position:relative;height:28px;display:flex;justify-content:space-between;
    align-items:flex-end;padding-left:19px;font-size:17.5px;line-height:22px}
  .price-list li::before{content:"";position:absolute;left:0;top:8px;width:10px;height:15px;background:var(--purple)}
  .price-list li::after{content:"";position:absolute;left:19px;right:0;bottom:-3px;height:1.5px;background:var(--rule)}
  .price-list li:last-child::after{display:none}
  .price-list .price{color:var(--purple)}
  .vaccines{top:365px}
  .extras{top:855px}
  .section-head{position:absolute;left:39px;top:686px;font-family:"Montserrat",Arial,sans-serif;
    font-weight:800;font-size:33px;color:var(--navy);letter-spacing:-0.5px}
  .tablet{position:absolute;left:57px;width:404px;padding-left:1px;font-size:17.5px;line-height:20px}
  .tablet::before{content:"";position:absolute;left:-18px;top:4px;width:7px;height:34px;background:var(--purple)}
  .tablet .rate{display:block;color:var(--purple)}
  .tablet.first{top:737px;padding-bottom:6px;border-bottom:1.5px solid var(--rule)}
  .tablet.second{top:785px}
  .also{position:absolute;left:57px;top:830px;font-size:19px;color:var(--red)}
  .photo{position:absolute;left:484px;width:364px}
  .photo.cold{top:368px;height:275px;background:linear-gradient(135deg,#e8e2dc,#c9b2a0 55%,#f1ece8)}
  .photo.pills{top:653px;height:274px;background:linear-gradient(135deg,#d7d9dc,#e58ab6 50%,#c7424f)}
  .photo.smoking{top:938px;height:262px;background:linear-gradient(135deg,#8fb2d8,#e6d2c6 50%,#5f86b8)}
  .notice{position:absolute;left:0;top:1022px;width:484px;height:107px;background:var(--footer-dark);
    color:#e6e6e6;font-size:14px;line-height:17px;text-align:center;padding:12px 50px 0}
  .contact{position:absolute;left:0;top:1129px;width:484px;height:71px;background:var(--navy);
    color:var(--white);text-align:center;padding-top:8px}
  .contact .call{font-family:"Montserrat",Arial,sans-serif;font-weight:700;font-size:17px;letter-spacing:0.2px}
  .contact .details{font-size:15px;margin-top:3px}
</style>
</head>
<body>
<main class="leaflet">
  <svg class="header" viewBox="0 0 848 320" aria-hidden="false">
    <defs>
      <linearGradient id="headerTone" x1="0" y1="0" x2="1" y2="0">
        <stop offset="0" stop-color="#3d4f9e"/>
        <stop offset="0.5" stop-color="#7a3f8e"/>
        <stop offset="1" stop-color="#d92a3a"/>
      </linearGradient>
    </defs>
    <rect width="848" height="320" fill="url(#headerTone)" role="img" aria-label="Photo of a family feeling unwell, tinted blue to red"/>
    <g fill="#f4f4f6">
      <path d="M0 180 C40 130 150 130 195 185 C215 150 280 150 320 180 C330 230 380 260 400 250 L430 300 L460 250 C500 260 540 240 560 200 C600 170 670 170 700 200 C730 170 800 165 848 190 L848 320 L0 320 Z"/>
    </g>
  </svg>
  <div class="brand"><span class="brand-dot"></span><span class="brand-name">Brackenmoor Travel Clinic</span></div>

  <h1 class="title">TRAVEL <span>VACCINES</span></h1>

  <ul class="price-list vaccines">
    <li>Cholera<span class="price">£25</span></li>
    <li>Diphtheria Tetanus and Polio<span class="price">£30</span></li>
    <li>Hepatitis A<span class="price">£40</span></li>
    <li>Hepatitis B<span class="price">£40</span></li>
    <li>Hepatitis A &amp; B (combined)<span class="price">£70</span></li>
    <li>Hepatitis A &amp; Typhoid (combined)<span class="price">£70</span></li>
    <li>Japanese Encephalitis<span class="price">£85</span></li>
    <li>Meningitis ACWY<span class="price">£50</span></li>
    <li>Rabies<span class="price">£60</span></li>
    <li>Tick Borne Encephaliti<span class="price">£60</span></li>
    <li>Typhoid<span class="price">£35</span></li>
  </ul>

  <h2 class="section-head">ANTIMALARIALS</h2>
  <p class="tablet first">Generic Malavex (Atovaquone/Proguanil)<span class="rate">£2 per tablet</span></p>
  <p class="tablet second">Doxycycline 100mg<span class="rate">50p per capsule</span></p>
  <p class="also">We also vaccinate against:</p>

  <ul class="price-list extras">
    <li>Chickenpox<span class="price">£60</span></li>
    <li>Measles Mumps &amp; Rubella (MMR)<span class="price">£40</span></li>
    <li>Meningitis B<span class="price">£110</span></li>
    <li>Shingles<span class="price">£150</span></li>
    <li>Human Papilloma Virus (HPV)<span class="price">£150</span></li>
  </ul>

  <div class="photo cold" role="img" aria-label="Photo of a woman with a cold wrapped in a blanket"></div>
  <div class="photo pills" role="img" aria-label="Photo of blister packs of pink and red tablets"></div>
  <div class="photo smoking" role="img" aria-label="Photo of hands breaking a cigarette in two"></div>

  <div class="notice">Prices are per dose &amp; more than one dose of vaccine may be needed<br>**The availability and price of the above may vary. During shortages wholesale prices can rise and we will inform you of any price changes.</div>
  <div class="contact">
    <p class="call">FOR MORE INFORMATION VISIT</p>
    <p class="details">www.brackenmoortravelclinic.co.uk or Call 01632 960417</p>
  </div>
</main>
</body>
</html>
```